Stationery Design Project

I would like to get the designs done for the following:
1. Envelop - Big (for A4 documents) and Small for Folded document.
2. Letterpad
3. Stationary Pad (for Internal Use)
Thanks,
Tushar
- We are open to different ideas and design concept, it should be unique and should still maintain a corporate look.
Velqo-Fulllogo - This is the complete logo set.
Velqo Logo Only - this is only the complete logo of the company
Velqo Arrow - Arrow is a minimum form of the logo, which represents "velqo"
Velqomin-Tag - Velqo Minimum name with the tag-line can be used also as a logo
Note: We have attached Velqo - Letter Pad Format - Sample.pdf file for just showing you an example for the letterpad.

```html
<!DOCTYPE html>
<html lang="en">
<head>
<meta charset="utf-8">
<title>Velqo Stationery</title>
<link href="https://fonts.googleapis.com/css2?family=Roboto:wght@300;400;500&display=swap" rel="stylesheet">
<style>
:root{
  --bg:#ececec;
  --paper:#fbfbfb;
  --ink:#4a4a4b;
  --ink-soft:#7a7a7b;
  --tone-mid:#6f6f70;
  --tone-light:#a5a5a6;
  --band:#9a9a9b;
}
*{margin:0;padding:0;box-sizing:border-box}
html,body{width:1200px;height:924px;overflow:hidden;background:var(--bg);font-family:"Roboto",Arial,sans-serif;color:var(--ink)}
.canvas{position:relative;width:1200px;height:924px}
.piece{position:absolute;background:var(--paper);box-shadow:0 1px 3px rgba(0,0,0,.12);overflow:hidden}
.wordmark{font-weight:300;color:var(--ink);line-height:1;letter-spacing:-.5px}
.tagline{font-weight:300;color:var(--ink-soft);line-height:1.1;white-space:nowrap}
.fine{font-size:4.5px;line-height:6.5px;color:var(--ink-soft);white-space:nowrap}
.fine b{font-weight:500;color:var(--ink)}
.footer-band{position:absolute;left:0;bottom:0;width:100%;background:var(--band)}
.tone-panel{position:absolute;inset:0}

/* letterhead */
.letterhead{left:222px;top:98px;width:356px;height:504px}
.letterhead .brand{position:absolute;right:34px;top:34px}
.letterhead .wordmark{font-size:24px}
.letterhead .tagline{font-size:8.5px}
.letterhead .address{position:absolute;right:34px;top:84px;text-align:right}
.letterhead .footer-band{height:9px}

/* folder */
.folder{left:640px;top:76px;width:420px;height:530px;background:var(--ink)}
.folder .tone-panel{background:linear-gradient(118deg,var(--ink) 0%,var(--ink) 52%,var(--tone-mid) 68%,var(--tone-light) 100%)}
.folder .brand{position:absolute;left:72px;top:80px}
.folder .wordmark{font-size:38px;color:#e4e4e4}
.folder .tagline{font-size:12px;color:#c4c4c5}
.folder .web{position:absolute;left:255px;top:468px;transform:rotate(-62deg);transform-origin:left top;font-size:15px;color:#e2e2e3;letter-spacing:.5px;font-weight:300;white-space:nowrap}
.folder .web b{font-weight:500}

/* business cards */
.card-front{left:95px;top:647px;width:160px;height:90px}
.card-front .brand{position:absolute;left:8px;top:40px}
.card-front .wordmark{font-size:18px}
.card-front .tagline{font-size:5.5px}
.card-front .person{position:absolute;left:90px;top:14px}
.card-front .person .name{font-size:5.5px;font-weight:500;color:var(--ink);line-height:7px}
.card-front .person .role{font-size:4px;color:var(--ink-soft);line-height:6px;margin-bottom:3px}
.card-front .footer-band{height:6px}
.card-back{left:95px;top:761px;width:160px;height:92px;background:var(--ink)}
.card-back .tone-panel{background:linear-gradient(118deg,var(--ink) 0%,var(--ink) 45%,var(--tone-mid) 70%,var(--tone-light) 100%)}
.card-back .brand{position:absolute;left:9px;top:16px}
.card-back .wordmark{font-size:15px;color:#e4e4e4}
.card-back .tagline{font-size:4.5px;color:#c4c4c5}
.card-back .contact{position:absolute;left:9px;bottom:10px;font-size:4.5px;line-height:6.5px;color:#dcdcdd}

/* compliment slip */
.slip{left:296px;top:662px;width:396px;height:190px}
.slip .brand{position:absolute;left:102px;top:114px}
.slip .wordmark{font-size:22px}
.slip .tagline{font-size:7.5px}
.slip .company{position:absolute;left:199px;top:140px}
.slip .footer-band{height:8px}

/* envelope */
.envelope{left:734px;top:660px;width:398px;height:190px}
.envelope svg{position:absolute;inset:0}
.envelope .flap-mark{position:absolute;left:0;width:100%;top:30px;text-align:center;font-size:8px;font-weight:300;color:#a9a9aa}
</style>
</head>
<body>
<main class="canvas">

  <section class="piece letterhead" aria-label="Letterhead">
    <div class="brand">
      <div class="wordmark">velqo</div>
      <div class="tagline">precisely progressive</div>
    </div>
    <div class="address fine">
      Plot No. 18, Kiran Park,<br>Vesu, Kelvapur - 482115<br>Dhoran, India<br>
      <b>Phone:</b> +91 261 4400712<br><b>Email:</b> info@velqo.co.in<br><b>Web:</b> www.velqo.co.in
    </div>
    <div class="footer-band"></div>
  </section>

  <section class="piece folder" aria-label="Presentation folder">
    <div class="tone-panel" role="img" aria-label="Soft grey tonal gradient across the cover"></div>
    <div class="brand">
      <div class="wordmark">velqo</div>
      <div class="tagline">precisely progressive</div>
    </div>
    <div class="web">www.<b>velqo</b>.co.in</div>
  </section>

  <section class="piece card-front" aria-label="Business card front">
    <div class="brand">
      <div class="wordmark">velqo</div>
      <div class="tagline">precisely progressive</div>
    </div>
    <div class="person">
      <div class="name">KUNAL MEHTA</div>
      <div class="role">Chairman &amp; Managing Director</div>
      <div class="fine"><b>Mobile:</b> +91 98250 41177<br><b>Email:</b> kunal@velqo.co.in<br>Plot No. 18, Kiran Park, Vesu<br>Kelvapur - 482115, India<br><b>Phone:</b> +91 261 4400712<br><b>Web:</b> www.velqo.co.in</div>
    </div>
    <div class="footer-band"></div>
  </section>

  <section class="piece card-back" aria-label="Business card back">
    <div class="tone-panel" role="img" aria-label="Soft grey tonal gradient across the card"></div>
    <div class="brand">
      <div class="wordmark">velqo</div>
      <div class="tagline">precisely progressive</div>
    </div>
    <div class="contact">+91 261 4400712 &nbsp; info@velqo.co.in &nbsp; www.velqo.co.in</div>
  </section>

  <section class="piece slip" aria-label="Compliment slip">
    <div class="brand">
      <div class="wordmark">velqo</div>
      <div class="tagline">precisely progressive</div>
    </div>
    <div class="company fine">
      <b>VELQO INDUSTRIES LIMITED</b><br>
      SY. 12, Kiran Park, Plot No. 18, Vesu Road - 482115, Kelvapur, India<br>
      <b>Phone:</b> +91 261 4400712 &nbsp;<b>Email:</b> info@velqo.co.in &nbsp;<b>Web:</b> www.velqo.co.in
    </div>
    <div class="footer-band"></div>
  </section>

  <section class="piece envelope" aria-label="Envelope">
    <svg viewBox="0 0 398 190">
      <polygon points="0,0 398,0 398,8 374,54 24,54 0,8" fill="var(--ink)"/>
    </svg>
    <div class="flap-mark">velqo</div>
  </section>

</main>
</body>
</html>
```